Modern, profession Order Insert Card for Head Shop/Smoke shop

We are looking for a modern design for our Order Insert cards where we will have some text thanking the customer for their order.
The design needs to be professional and modern, showing our logo (SVG attached) and our website URL.
Our eCommerce store sells "head shop" items, things like bongs, rolling papers, cbd products, disposable vapes, etc.
I have uploaded 2 versions of our logo, one featuring the colour of green we use across our brand, a black logo or the logo can be inverted to be a white logo on a black background.
Target Market(s)
The websites target audience is anyone needing accessories or tools to consume medicinal marijuana/the consumers favourite herbs or any one in the vaping community.
Contact Information for Business Card
Website URL, Space for a small thank you note and our logo.
Look and feel

```html
<!DOCTYPE html>
<html lang="en">
<head>
<meta charset="utf-8">
<title>Order Insert Card – Greenloft</title>
<link rel="stylesheet" href="https://fonts.googleapis.com/css2?family=Kaushan+Script&family=Montserrat:wght@600&display=swap">
<style>
  :root {
    --backdrop: #2b2b2b;
    --card-light: #ecffb4;
    --card-mid: #cfe98c;
    --card-dark: #96c43a;
    --ink: #161616;
  }
  html, body {
    margin: 0;
    padding: 0;
    width: 1200px;
    height: 934px;
    overflow: hidden;
    background: var(--backdrop);
  }
  .canvas {
    position: relative;
    width: 1200px;
    height: 934px;
  }
  .insert-card {
    position: absolute;
    left: 100px;
    top: 158px;
    width: 1000px;
    height: 618px;
    background: linear-gradient(28deg, var(--card-dark) 0%, var(--card-mid) 45%, var(--card-light) 85%);
    overflow: hidden;
  }
  .brand {
    position: absolute;
    left: 72px;
    top: 84px;
    display: flex;
    align-items: center;
    gap: 14px;
  }
  .brand-dot {
    width: 22px;
    height: 22px;
    border-radius: 50%;
    background: var(--ink);
  }
  .brand-name {
    font-family: "Montserrat", sans-serif;
    font-weight: 600;
    font-size: 36px;
    letter-spacing: 1px;
    color: var(--ink);
  }
  .thanks {
    position: absolute;
    left: 70px;
    top: 178px;
    margin: 0;
    font-family: "Kaushan Script", cursive;
    font-weight: 400;
    font-size: 112px;
    line-height: 132px;
    color: var(--ink);
  }
  .thanks span { display: block; }
  .website {
    position: absolute;
    left: 72px;
    top: 540px;
    font-family: "Montserrat", sans-serif;
    font-weight: 600;
    font-size: 26px;
    letter-spacing: 2px;
    color: var(--ink);
  }
</style>
</head>
<body>
  <div class="canvas">
    <section class="insert-card">
      <div class="brand">
        <span class="brand-dot"></span>
        <span class="brand-name">GREENLOFT</span>
      </div>
      <h1 class="thanks"><span>Thank you</span><span>very much !</span></h1>
      <div class="website">www.greenloftsupply.com</div>
    </section>
  </div>
</body>
</html>
```